Chimney Service company needs new business card design

We need a updated business card with our new logo added. We provide a full range of chimney services throughout Vermont and New Hampshire. The business card will be one sided and color. Attached is our current business card another document showing all the information we would like on the card.
We dont like a lot of flashy colors.... here is a link to our website to get an idea of our branding www.flueguardnorthvt-example.com

Target Market(s)

homeowners

Industry/Entity Type

Business

Contact Information for Business Card

See attached sheet for content.

Font styles to use
Serif
Sans Serif

Requirements
Must have
• all information provided on separate sheet
Should not have
• Additional information that may clogg up design

```html
<!DOCTYPE html>
<html lang="en">
<head>
<meta charset="utf-8">
<title>Flueguard North – Business Card</title>
<link href="https://fonts.googleapis.com/css2?family=Open+Sans:wght@400;600&display=swap" rel="stylesheet">
<style>
  :root {
    --page: #e9e7e4;
    --card-white: #ffffff;
    --card-fade: #e6e6e6;
    --dark-1: #262626;
    --dark-2: #4a4a4a;
    --ink: #3a3a3a;
    --accent: #c1272d;
    --light-text: #f2f2f2;
  }
  * { margin: 0; padding: 0; box-sizing: border-box; }
  html, body { width: 1200px; height: 1023px; overflow: hidden; background: var(--page); }
  body { display: flex; align-items: center; justify-content: center; font-family: "Open Sans", sans-serif; }

  .card {
    position: relative;
    width: 1050px; height: 600px;
    border-radius: 26px;
    overflow: hidden;
    background: linear-gradient(180deg, var(--card-white) 0%, var(--card-fade) 52%);
    box-shadow: 0 14px 40px rgba(0,0,0,.18);
  }

  .brand-name {
    position: absolute; left: 80px; top: 120px;
    font-family: "Open Sans", sans-serif; font-weight: 600; font-size: 58px;
    color: var(--ink); letter-spacing: 2px; line-height: 1;
  }

  .dark-panel {
    position: absolute; left: 0; right: 0; top: 305px; bottom: 0;
    background: linear-gradient(100deg, var(--dark-2) 0%, var(--dark-1) 70%);
  }

  .region-tag {
    position: absolute; left: 150px; top: 272px; height: 54px; padding: 0 26px;
    display: flex; align-items: center;
    background: var(--accent); color: #fff; font-size: 27px; border: 3px solid #fff;
  }

  .credentials { position: absolute; left: 70px; top: 372px; color: var(--light-text); }
  .credentials p { font-size: 22px; font-weight: 600; text-transform: uppercase; line-height: 34px; }

  .contact { position: absolute; left: 70px; top: 460px; list-style: none; color: var(--light-text); }
  .contact li { display: flex; align-items: center; gap: 14px; font-size: 25px; line-height: 40px; }
  .contact svg { width: 18px; height: 18px; fill: var(--light-text); flex: none; }

  .services { position: absolute; left: 620px; top: 350px; color: var(--light-text); }
  .services h2 { font-size: 26px; font-weight: 400; color: var(--accent); text-transform: uppercase; margin-bottom: 6px; }
  .services ul { list-style: none; }
  .services li { font-size: 24px; line-height: 38px; display: flex; align-items: center; gap: 14px; }
  .services li::before { content: ""; width: 11px; height: 11px; border-radius: 50%; background: var(--accent); }
</style>
</head>
<body>
  <article class="card">
    <h1 class="brand-name">FLUEGUARD NORTH</h1>

    <div class="dark-panel"></div>
    <div class="region-tag">Serving VT and New Hampshire since 1989</div>

    <div class="credentials">
      <p>Fully insured – Free estimates</p>
      <p>Family owned and operated</p>
    </div>

    <ul class="contact">
      <li><svg viewBox="0 0 24 24"><path d="M6.6 10.8a15.1 15.1 0 0 0 6.6 6.6l2.2-2.2c.3-.3.7-.4 1-.2 1.1.4 2.3.6 3.6.6.6 0 1 .4 1 1V20c0 .6-.4 1-1 1A17 17 0 0 1 3 4c0-.6.4-1 1-1h3.5c.6 0 1 .4 1 1 0 1.3.2 2.5.6 3.6.1.3 0 .7-.2 1z"/></svg>802-555-0147</li>
      <li><svg viewBox="0 0 24 24"><path d="M2 5h20v14H2zm2 2v.5l8 5 8-5V7zm0 3v7h16v-7l-8 5z"/></svg>info@flueguardnorthvt-example.com</li>
      <li><svg viewBox="0 0 24 24"><path d="M12 2a10 10 0 1 0 0 20 10 10 0 0 0 0-20zm0 2c.9 1.2 1.7 3 2 5h-4c.3-2 1.1-3.8 2-5zM4.3 13a8 8 0 0 1 0-2h3.8a17 17 0 0 0 0 2zm5.7 0a15 15 0 0 1 0-2h4a15 15 0 0 1 0 2zm6 0a17 17 0 0 0 0-2h3.7a8 8 0 0 1 0 2zm-6 2h4c-.3 2-1.1 3.8-2 5-.9-1.2-1.7-3-2-5z"/></svg>www.flueguardnorthvt-example.com</li>
    </ul>

    <section class="services">
      <h2>Services we provide</h2>
      <ul>
        <li>Full Masonry Services</li>
        <li>Historic chimney restoration</li>
        <li>Stainless steel liners</li>
        <li>New Chimney installations</li>
        <li>FSCB Certified Chimney sweeps</li>
      </ul>
    </section>
  </article>
</body>
</html>
```